Visitenkarten-Design für Sonnen-/Fensterschutz
Zielgruppe
KLR GmbH ist eine Firma, die Sonnenschutz und Fensterschutz anbieten.
'Ihr kompetenter Partner in Sachen Sonnenschutz- , Fenster- und Türtechnik. Sie erhalten echtes Handwerk aus dem Mühlviertel zu fairen Preisen.'
Unsere Zielgruppe sind Personen mit Haus, die am Land leben.
Firmenname: KLR GmbH
Slogan: Fenster & Sonnenschutz
Aufgabenstellung
Hier befindet sich das Logodesign: https://dl.qv/t-Rm8pQ2wZtB
Bitte ein schlichtes Design bereitstellen mit einer Dummy-Person:
Lutz Brenneke + Telefonnummer + Email
Die finalen Daten bitte erst am Schluss berücksichtigen (für Gewinnerdesign)
Gerne auch hintern + vorne bedruckbar bereitstellen.

```html
<!DOCTYPE html>
<html lang="de">
<head>
<meta charset="utf-8">
<title>KLR GmbH – Visitenkarte</title>
<link href="https://fonts.googleapis.com/css2?family=Open+Sans:wght@400;600;700&display=swap" rel="stylesheet">
<style>
  :root {
    --page-bg: #e9e6e3;
    --card-white: #ffffff;
    --card-grey: #e4e4e4;
    --brand-red: #d8352a;
    --brand-orange: #e8642c;
    --back-top: #e2522f;
    --back-bottom: #c0281f;
    --ink: #1d1d1d;
    --ink-soft: #444444;
    --white: #ffffff;
  }
  * { box-sizing: border-box; margin: 0; padding: 0; }
  html, body {
    width: 1200px; height: 800px; overflow: hidden;
    background: var(--page-bg);
    font-family: "Open Sans", Arial, sans-serif;
  }
  .sheet {
    position: relative; width: 1200px; height: 800px;
    display: flex; align-items: center; justify-content: center; gap: 60px;
  }
  .card {
    position: relative; width: 525px; height: 300px;
    border-radius: 3px;
    box-shadow: 0 10px 28px rgba(0,0,0,.18), 0 2px 6px rgba(0,0,0,.12);
    overflow: hidden;
  }

  /* Front side */
  .card-front {
    background: linear-gradient(135deg, var(--card-white) 0%, var(--card-white) 45%, var(--card-grey) 100%);
  }
  .front-header {
    position: absolute; left: 40px; top: 48px;
    display: flex; align-items: center; gap: 18px;
  }
  .brand-mini {
    display: flex; align-items: center; gap: 8px;
    font-weight: 700; font-size: 17px; color: var(--brand-red);
    white-space: nowrap;
  }
  .brand-mini .dot {
    width: 12px; height: 12px; background: var(--brand-red);
  }
  .divider {
    width: 2px; height: 58px; background: var(--brand-red);
    transform: skewX(-22deg);
  }
  .person-name {
    font-size: 27px; font-weight: 600; color: var(--brand-red); line-height: 1.15;
    white-space: nowrap;
  }
  .person-role {
    font-size: 25px; font-weight: 400; color: var(--ink); line-height: 1.15;
  }
  .contact-list {
    position: absolute; right: 40px; top: 142px;
    list-style: none; font-size: 13px; color: var(--ink-soft);
  }
  .contact-list li {
    display: flex; align-items: center; gap: 10px; margin-bottom: 9px;
    white-space: nowrap;
  }
  .contact-list li.web { font-weight: 700; color: var(--ink); }
  .contact-list svg { width: 14px; height: 14px; flex: none; }
  .front-brand {
    position: absolute; left: 40px; bottom: 38px;
  }
  .brand-name {
    font-weight: 700; font-size: 40px; color: var(--brand-orange); line-height: 1;
    white-space: nowrap;
  }
  .brand-slogan {
    font-size: 12px; font-weight: 600; letter-spacing: .04em;
    color: var(--brand-orange); margin-top: 6px; text-transform: uppercase;
  }

  /* Back side */
  .card-back {
    background: linear-gradient(150deg, var(--back-top) 0%, var(--brand-orange) 50%, var(--back-bottom) 100%);
    display: flex; align-items: center; justify-content: center;
  }
  .back-brand { display: flex; align-items: center; gap: 16px; }
  .back-brand .square {
    width: 30px; height: 30px; border: 3px solid var(--white);
  }
  .back-brand .brand-name { color: var(--white); font-size: 52px; }
  .back-brand .brand-slogan { color: var(--white); font-size: 13px; }
</style>
</head>
<body>
<main class="sheet">
  <section class="card card-front" aria-label="Vorderseite">
    <header class="front-header">
      <div class="brand-mini"><span class="dot"></span>KLR GmbH</div>
      <span class="divider"></span>
      <div>
        <p class="person-name">Lutz Brenneke</p>
        <p class="person-role">Director</p>
      </div>
    </header>

    <ul class="contact-list">
      <li>
        <svg viewBox="0 0 16 16"><circle cx="8" cy="8" r="8" fill="#d8352a"/><path d="M5.2 4.5l1.4-.3.8 1.9-.9.7a5 5 0 0 0 2.5 2.5l.7-.9 1.9.8-.3 1.4c-3.4.2-6.3-2.7-6.1-6.1z" fill="#fff"/></svg>
        0111 4826105374
      </li>
      <li>
        <svg viewBox="0 0 16 16"><circle cx="8" cy="8" r="8" fill="#d8352a"/><rect x="4" y="5" width="8" height="6" fill="none" stroke="#fff" stroke-width="1.2"/><path d="M4 5l4 3.2L12 5" fill="none" stroke="#fff" stroke-width="1.2"/></svg>
        lutz@klr-fenster.de
      </li>
      <li class="web">
        <svg viewBox="0 0 16 16"><circle cx="8" cy="8" r="8" fill="#d8352a"/><circle cx="8" cy="8" r="4.5" fill="none" stroke="#fff" stroke-width="1"/><ellipse cx="8" cy="8" rx="2" ry="4.5" fill="none" stroke="#fff" stroke-width="1"/><path d="M3.5 8h9" stroke="#fff" stroke-width="1"/></svg>
        www.klr-fenster.de
      </li>
    </ul>

    <div class="front-brand">
      <p class="brand-name">KLR GmbH</p>
      <p class="brand-slogan">Fenster &amp; Sonnenschutz</p>
    </div>
  </section>

  <section class="card card-back" aria-label="Rückseite">
    <div class="back-brand">
      <span class="square"></span>
      <div>
        <p class="brand-name">KLR GmbH</p>
        <p class="brand-slogan">Fenster &amp; Sonnenschutz</p>
      </div>
    </div>
  </section>
</main>
</body>
</html>
```